Drifting Past Solvane website

A very basic website using the graphics provided. The site would give the user the ability to read a description of the book, read testimonials, About the author, Read chapter 1, link to vendoro, order direct via coinlet.

```html
<!DOCTYPE html>
<html lang="en">
<head>
<meta charset="utf-8">
<title>Drifting Past Solvane</title>
<link href="https://fonts.googleapis.com/css2?family=Cinzel:wght@400;600;700&display=swap" rel="stylesheet">
<style>
:root{
  --ink:#1a1a1a;
  --grey-text:#555;
  --icon-grey:#8a8a8a;
  --nav-top:#5a5a5e;
  --nav-bottom:#1c1c1f;
  --black:#000;
  --gold:#f2d77a;
  --orange:#f39a1c;
  --silver:#c9c9c9;
  --line:#cfcfcf;
  --footer:#050505;
  --white:#fff;
}
*{box-sizing:border-box;margin:0;padding:0}
html,body{width:978px;height:1200px;overflow:hidden;background:var(--white)}
body{position:relative;font-family:Arial,Helvetica,sans-serif;color:var(--ink)}
.serif{font-family:'Cinzel',serif}
.abs{position:absolute}

.site-title{left:141px;top:26px;font-family:'Cinzel',serif;color:var(--ink);line-height:1}
.site-title .line1{font-size:24px;letter-spacing:1px}
.site-title .line2{font-size:28px;margin-top:6px;letter-spacing:1px}

.follow{right:141px;top:56px;display:flex;align-items:center;gap:5px}
.follow-label{font-family:'Cinzel',serif;font-size:12px;margin-right:6px;letter-spacing:.5px}
.social{width:24px;height:24px;border-radius:50%;background:var(--icon-grey);color:var(--white);font-family:'Cinzel',serif;font-size:11px;font-weight:700;display:flex;align-items:center;justify-content:center;margin-left:5px}

.main-nav{left:141px;top:102px;width:698px;height:36px;background:linear-gradient(var(--nav-top),var(--nav-bottom));border-bottom:2px solid #9a9a9a;display:flex;align-items:center}
.main-nav a{font-family:'Cinzel',serif;color:var(--white);text-decoration:none;font-size:12.5px;letter-spacing:.5px;position:absolute;top:11px}

.hero{left:141px;top:144px;width:698px;height:309px;background:radial-gradient(ellipse at 40% 40%,#3a3a3a 0%,#111 55%,#000 100%);overflow:hidden}
.hero-text{left:60px;width:300px;top:36px;text-align:center}
.hero-text .h1{font-family:'Cinzel',serif;color:var(--gold);font-size:30px;letter-spacing:1px}
.hero-text .h2{font-family:'Cinzel',serif;color:var(--orange);font-size:30px;font-weight:700;margin-top:8px;line-height:1}
.hero-text .author{font-family:'Cinzel',serif;color:var(--silver);font-size:19px;font-weight:700;margin-top:8px;letter-spacing:1px}
.hero-text p{color:#bbb;font-size:9.5px;line-height:19.5px;margin-top:10px}
.btn-silver{background:linear-gradient(#f4f4f4,#9c9c9c);color:#111;font-family:'Cinzel',serif;border:1px solid #777;display:flex;align-items:center;justify-content:center}
.hero-btn{left:135px;top:235px;width:172px;height:39px;font-size:14px;letter-spacing:1px}
.hero-book{left:443px;top:20px;width:188px;height:272px;background:linear-gradient(160deg,#4a2a22,#1a1a1a 60%,#2c3c4a)}
.slider-arrows{display:flex;gap:2px}
.slider-arrows span{width:18px;height:20px;background:#3a3a3a;color:#aaa;font-size:11px;display:flex;align-items:center;justify-content:center}

.about-book{left:150px;top:482px;width:194px;height:286px;background:linear-gradient(160deg,#4a2a22,#1a1a1a 55%,#3a4e5e)}
.about{left:379px;top:502px;width:460px}
.section-title{font-family:'Cinzel',serif;font-size:20px;letter-spacing:1px;color:var(--ink)}
.about p{font-size:8.5px;line-height:16.8px;color:var(--grey-text);margin-top:17px}
.about p + p{margin-top:17px}
.btn-dark{background:linear-gradient(#333,#050505);color:var(--white);font-family:'Cinzel',serif;font-size:10.5px;display:flex;align-items:center;justify-content:center;border-radius:2px}
.read-more{left:379px;top:685px;width:112px;height:32px}

.chapter{left:141px;top:774px;width:698px;height:136px;background:var(--black)}
.chapter-frame{left:7px;top:7px;right:7px;bottom:7px;border:1px solid #444}
.chapter-art{left:38px;top:24px;width:100px;height:86px;background:linear-gradient(135deg,#ddd,#8a9a7a)}
.chapter-title{left:162px;top:24px;font-family:'Cinzel',serif;color:var(--white);font-size:21px;letter-spacing:1px}
.chapter p{left:164px;top:62px;width:380px;color:#888;font-size:8.3px;line-height:16.8px}
.click-here{left:551px;top:61px;width:122px;height:39px;font-size:12.5px}

.testimonials-title{left:141px;top:942px}
.testi-arrows{left:568px;top:944px}
.testi-arrows span{width:15px;height:15px;background:#aaa;color:var(--white)}
.testimonial{top:986px;width:230px;height:110px}
.avatar{left:5px;top:0;width:64px;height:64px;border-radius:50%;background:radial-gradient(#d9c2b0,#9bb4cf)}
.t-name{left:2px;top:78px;font-family:'Cinzel',serif;font-size:9px;color:var(--ink)}
.t-date{left:13px;top:94px;font-family:'Cinzel',serif;font-size:7.5px;color:#777}
.quote-mark{font-family:Georgia,serif;font-size:22px;color:#c8c8c8}
.t-text{left:98px;top:11px;width:120px;font-size:8.5px;line-height:16px;color:var(--grey-text)}

.vendor{left:648px;width:191px;height:71px;border:1px solid var(--line);display:flex;align-items:center;justify-content:center;font-family:'Cinzel',serif;font-weight:700;font-size:28px;color:var(--ink)}

.footer{left:0;top:1126px;width:978px;height:74px;background:var(--footer)}
.footer a{position:absolute;top:20px;font-family:'Cinzel',serif;color:#bbb;text-decoration:none;font-size:9px;letter-spacing:.5px}
.copyright{left:0;top:44px;width:978px;text-align:center;font-family:'Cinzel',serif;color:#bbb;font-size:8.5px}
</style>
</head>
<body>

<header>
  <div class="abs site-title">
    <div class="line1">Drifting Past</div>
    <div class="line2">SOLVANE</div>
  </div>
  <div class="abs follow">
    <span class="follow-label">Follow Us :</span>
    <span class="social" aria-label="Friendlo">F</span>
    <span class="social" aria-label="Plusway">P</span>
    <span class="social" aria-label="Pinbay">P</span>
    <span class="social" aria-label="Clipstream">C</span>
    <span class="social" aria-label="Chirpo">C</span>
    <span class="social" aria-label="Workly">W</span>
  </div>
</header>

<nav class="abs main-nav">
  <a href="#" style="left:34px">Home</a>
  <a href="#" style="left:122px">About Us</a>
  <a href="#" style="left:230px">Testimonials</a>
  <a href="#" style="left:362px">My Book</a>
  <a href="#" style="left:469px">Blog</a>
  <a href="#" style="left:553px">Contact Us</a>
</nav>

<section class="abs hero">
  <div class="abs hero-text">
    <div class="h1">DRIFTING PAST</div>
    <div class="h2">SOLVANE</div>
    <div class="author">ROWAN HALE</div>
    <p>It is a long established fact that a reader will be distracted by the readable content of a page when looking at its layout. The point of using Lorem Ipsum is that it has a more-or-less normal distribution of letters...</p>
  </div>
  <a class="abs btn-silver hero-btn" href="#">MY NEW BOOK</a>
  <div class="abs hero-book" role="img" aria-label="Book cover: a man silhouetted behind barred window overlooking a tropical beach"></div>
  <div class="abs slider-arrows" style="left:648px;top:278px"><span>&lsaquo;</span><span>&rsaquo;</span></div>
</section>

<section>
  <div class="abs about-book" role="img" aria-label="3D book cover of Drifting Past Solvane by Rowan Hale"></div>
  <div class="abs about">
    <h2 class="section-title">About the Author</h2>
    <p>It is a long established fact that a reader will be distracted by the readable content of a page when looking at its layout. The point of using Lorem Ipsum is that it has a more-or-less normal distribution of letters, as opposed to using 'Content here, content here', making it look like readable English. Many desktop publishing packages and web page editors now use Lorem Ipsum as their default model text, and a search for 'lorem ipsum' will uncover many web sites still in their infancy. Various versions have evolved over the years, sometimes by accident, sometimes on purpose.</p>
    <p>It is a long established fact that a reader will be distracted by the readable content of a page when looking at its layout. The point of using Lorem Ipsum is that it has a more-or-less normal distribution of letters...</p>
  </div>
  <a class="abs btn-dark read-more" href="#">Read more</a>
</section>

<section class="abs chapter">
  <div class="abs chapter-frame"></div>
  <div class="abs chapter-art" role="img" aria-label="Open book with reading glasses"></div>
  <h2 class="abs chapter-title">Read Chapter 1</h2>
  <p class="abs">It is a long established fact that a reader will be distracted by the readable content of a page when looking at its layout. The point of using Lorem Ipsum is that it has a more-or-less normal distribution of letters, as opposed to using 'Content here...</p>
  <a class="abs btn-silver click-here" href="#">Click Here</a>
</section>

<section>
  <h2 class="abs section-title testimonials-title">Testimonials</h2>
  <div class="abs slider-arrows testi-arrows"><span>&lsaquo;</span><span>&rsaquo;</span></div>

  <div class="abs testimonial" style="left:141px">
    <div class="abs avatar" role="img" aria-label="Portrait photo of reviewer"></div>
    <div class="abs t-name">Milo Farrant</div>
    <div class="abs t-date">27 Mar 2014</div>
    <span class="abs quote-mark" style="left:78px;top:-4px">&ldquo;</span>
    <p class="abs t-text">Lorem ipsum dolor sit amet, consectetur adipiscing elit. Donec tempor nibh eget orci tincidunt...</p>
    <span class="abs quote-mark" style="left:204px;top:72px">&rdquo;</span>
  </div>

  <div class="abs testimonial" style="left:382px">
    <div class="abs avatar" role="img" aria-label="Portrait photo of reviewer"></div>
    <div class="abs t-name" style="left:6px">Milo Farrant</div>
    <div class="abs t-date" style="left:15px">27 Mar 2014</div>
    <span class="abs quote-mark" style="left:78px;top:-4px">&ldquo;</span>
    <p class="abs t-text">Lorem ipsum dolor sit amet, consectetur adipiscing elit. Donec tempor nibh eget orci tincidunt...</p>
    <span class="abs quote-mark" style="left:204px;top:72px">&rdquo;</span>
  </div>

  <a class="abs vendor" href="#" style="top:946px">vendoro</a>
  <a class="abs vendor" href="#" style="top:1024px">coinlet</a>
</section>

<footer class="abs footer">
  <a href="#" style="left:254px">Home</a>
  <a href="#" style="left:325px">About Us</a>
  <a href="#" style="left:412px">Testimonials</a>
  <a href="#" style="left:518px">My Book</a>
  <a href="#" style="left:603px">Blog</a>
  <a href="#" style="left:669px">Contact Us</a>
  <div class="abs copyright">&copy; 2014 My New Book. All Rights Reserved.</div>
</footer>

</body>
</html>
```